Premium Audio and HD Video with AFS!

AFS is a mobile studio that provides premium audio and HD video recording for the classical and jazz community in the Boston area. Specializing in concerts, recitals, auditions, studio releases, lectures, podcasts and more.
My website:
http://amberfieldsoundworks.example
https://www.facebook.com/AFSoundworks/
Target Market(s)
classical and jazz instrumentalists, vocalists, ensembles, choruses, a cappella groups, podcasters
Industry/Entity Type
Audio
Font styles to use
Serif
Colors
Designer to choose colors to be used in the design.
Requirements
Must have
- My logo!
- Must convey that this mobile recording studio is for classical and jazz musicians... not rock bands etc.
- I provide event recording as well as "studio recording" (for CDs etc)
- Eye catching
- Must be scalable for different size flyers... full page, half page etc
- I will use it for bulletin boards.. so the front side is most important... if the design is two sided, the lesser important info should be on the back side.
Nice to have
- Use some of the photos on my facebook page? Not sure they are high res or decent photos..
- https://www.facebook.com/AFSoundworks/
Should not have
- Anything depicting a rock band or similar

```html
<!DOCTYPE html>
<html lang="en">
<head>
<meta charset="utf-8">
<title>Amber Field Soundworks Flyer</title>
<link href="https://fonts.googleapis.com/css2?family=Cinzel:wght@400;600&family=Cormorant+SC:wght@500;600&display=swap" rel="stylesheet">
<style>
  :root {
    --ink: #050505;
    --paper: #f3efe6;
    --green: #7fbf9a;
    --green-deep: #1f4a35;
    --green-band: #2e6a4c;
    --tick: #8fd0a6;
  }
  * { margin: 0; padding: 0; box-sizing: border-box; }
  html, body { width: 857px; height: 1200px; overflow: hidden; background: var(--ink); }
  .flyer {
    position: relative; width: 857px; height: 1200px; background: var(--ink);
    color: var(--paper); font-family: "Cormorant SC", Georgia, serif; overflow: hidden;
  }
  .hero-photo {
    position: absolute; left: 0; top: 0; width: 857px; height: 620px;
    background:
      linear-gradient(180deg, transparent 55%, var(--ink) 100%),
      radial-gradient(ellipse 230px 200px at 140px 470px, rgba(170,22,28,.9), transparent 72%),
      radial-gradient(ellipse 200px 300px at 720px 280px, rgba(200,140,100,.55), transparent 72%),
      radial-gradient(ellipse 170px 260px at 200px 220px, rgba(140,90,60,.5), transparent 72%),
      radial-gradient(ellipse 200px 230px at 460px 170px, rgba(160,110,80,.55), transparent 72%),
      radial-gradient(ellipse 340px 160px at 520px 400px, rgba(120,60,40,.5), transparent 75%),
      linear-gradient(180deg, #2a1a12 0%, #1a100b 55%, var(--ink) 100%);
  }
  .brand {
    position: absolute; top: 455px; left: 0; width: 100%; text-align: center;
  }
  .brand-name {
    display: inline-flex; align-items: center; gap: 16px;
    font-family: "Cinzel", Georgia, serif; font-weight: 600; font-size: 54px;
    color: var(--green); letter-spacing: 2px; white-space: nowrap;
  }
  .brand-dot { width: 24px; height: 24px; border-radius: 50%; background: var(--green); }
  .brand-rule {
    width: 520px; height: 2px; margin: 14px auto 0; background: var(--green); opacity: .7;
  }
  .intro {
    position: absolute; top: 592px; left: 0; width: 100%; text-align: center;
    font-size: 31px; line-height: 1.25; letter-spacing: 1px;
  }
  .services {
    position: absolute; top: 690px; left: 105px; width: 668px;
    display: grid; grid-template-columns: 334px 334px; row-gap: 12px;
    list-style: none; font-family: "Cinzel", Georgia, serif; font-size: 28px; letter-spacing: 1px;
  }
  .services li { display: flex; align-items: center; gap: 14px; white-space: nowrap; }
  .services svg { width: 26px; height: 26px; flex: none; }
  .audience {
    position: absolute; top: 900px; left: 0; width: 100%; height: 150px;
    background: linear-gradient(180deg, var(--green-band), var(--green-deep));
    text-align: center; padding-top: 16px;
    border-top: 2px solid var(--green); border-bottom: 2px solid var(--green);
  }
  .audience-lead { font-size: 23px; letter-spacing: 2px; color: #b4e3c6; }
  .audience-list { font-size: 28px; line-height: 1.15; margin-top: 4px; }
  .contact {
    position: absolute; top: 1100px; left: 0; width: 100%; text-align: center;
    font-family: "Cinzel", Georgia, serif; font-size: 29px; letter-spacing: 1px; white-space: nowrap;
  }
</style>
</head>
<body>
<main class="flyer">
  <div class="hero-photo" role="img" aria-label="Photo of a classical string ensemble performing in warm stage light, with a vintage studio microphone in the lower left"></div>

  <div class="brand">
    <span class="brand-name"><span class="brand-dot"></span>Amber Field Soundworks</span>
    <div class="brand-rule"></div>
  </div>

  <p class="intro">Amber Field Provides<br>Audio and Video Production Services for</p>

  <ul class="services">
    <li><svg viewBox="0 0 24 24"><path d="M3 13l6 6L21 5" fill="none" stroke="var(--tick)" stroke-width="3.5" stroke-linecap="round" stroke-linejoin="round"/></svg>Concerts</li>
    <li><svg viewBox="0 0 24 24"><path d="M3 13l6 6L21 5" fill="none" stroke="var(--tick)" stroke-width="3.5" stroke-linecap="round" stroke-linejoin="round"/></svg>Auditions</li>
    <li><svg viewBox="0 0 24 24"><path d="M3 13l6 6L21 5" fill="none" stroke="var(--tick)" stroke-width="3.5" stroke-linecap="round" stroke-linejoin="round"/></svg>Recitals</li>
    <li><svg viewBox="0 0 24 24"><path d="M3 13l6 6L21 5" fill="none" stroke="var(--tick)" stroke-width="3.5" stroke-linecap="round" stroke-linejoin="round"/></svg>Lectures</li>
    <li><svg viewBox="0 0 24 24"><path d="M3 13l6 6L21 5" fill="none" stroke="var(--tick)" stroke-width="3.5" stroke-linecap="round" stroke-linejoin="round"/></svg>Studio Releases</li>
    <li><svg viewBox="0 0 24 24"><path d="M3 13l6 6L21 5" fill="none" stroke="var(--tick)" stroke-width="3.5" stroke-linecap="round" stroke-linejoin="round"/></svg>Podcasts &amp; More</li>
  </ul>

  <section class="audience">
    <p class="audience-lead">SERVING THE</p>
    <p class="audience-list">Solo Vocal/Instrumental, Chamber Music,<br>Choral, Orchestral, and Contemporary<br>acappella communities</p>
  </section>

  <p class="contact">AMBERFIELDSOUNDWORKS.EXAMPLE | 508.555.0142</p>
</main>
</body>
</html>
```